Qorta Labs

I am a CBD Manufacturer I would have a site more laid out in a lab format
current site is qortalabs-example.com what Id like is a site like brimwoodlabs-example.com

Target Market(s)

Any one needing cbd oil and finished goods

Coding

Coded - Design and coding required

Number of Pages Required

1 page

```html
<!DOCTYPE html>
<html lang="en">
<head>
<meta charset="UTF-8">
<title>Qorta Labs — CBD Manufacturer</title>
<link href="https://fonts.googleapis.com/css2?family=Roboto:wght@300;400;500;700;900&family=Open+Sans:wght@400;600&display=swap" rel="stylesheet">
<style>
:root{
  --ink:#1d1d1f;
  --text:#555;
  --muted:#8a8a8a;
  --line:#dcdcdc;
  --bg:#ffffff;
  --soft:#f2f2f2;
  --softer:#f7f7f7;
  --dark:#222326;
  --leaf:#4f8a2c;
  --amber:#d9a441;
  --notice:#e8483b;
}
*{box-sizing:border-box;margin:0;padding:0}
html,body{width:1200px;height:2996px;overflow:hidden}
body{background:var(--bg);font-family:"Open Sans",Arial,sans-serif;color:var(--text);font-size:13px;line-height:1.6;position:relative}
h1,h2,h3,h4,.brand,.btn,.nav a{font-family:"Roboto",Arial,sans-serif}
.btn{display:inline-block;background:var(--dark);color:#fff;font-size:11px;font-weight:500;padding:9px 20px;text-decoration:none;letter-spacing:.3px}
.btn.light{background:#fff;color:var(--ink);border:1px solid var(--line)}
.section-title{display:flex;align-items:center;justify-content:center;gap:14px;font-size:18px;font-weight:700;color:var(--ink);letter-spacing:1px}
.section-title::before,.section-title::after{content:"";width:30px;height:2px;background:var(--ink)}
.ph{position:absolute}

/* header */
.site-header{position:absolute;top:0;left:0;width:1200px;height:64px;background:#fff;display:flex;align-items:center;padding:0 80px;border-bottom:1px solid #eee;z-index:2}
.brand{font-size:20px;font-weight:700;color:var(--ink);letter-spacing:1px}
.nav{display:flex;gap:30px;margin-left:auto;margin-right:36px}
.nav a{font-size:12px;color:#444;text-decoration:none}
.nav a.active{font-weight:700;color:var(--ink);border-bottom:2px solid var(--ink);padding-bottom:3px}
.login{background:var(--dark);color:#fff;font-size:11px;padding:6px 14px;display:flex;gap:6px;align-items:center;font-family:"Roboto",sans-serif}
.cart{margin-left:20px;display:flex;align-items:center}

/* hero */
.hero{position:absolute;top:64px;left:0;width:1200px;height:456px;background:linear-gradient(90deg,#f4f4f4 0%,#eceeea 45%,#e6ebe0 100%)}
.hero-art{left:520px;top:0;width:680px;height:456px;background:radial-gradient(circle at 65% 55%,#e7b655 0%,#d9a441 12%,rgba(217,164,65,0) 30%),radial-gradient(circle at 30% 30%,#6aa33c 0%,rgba(106,163,60,0) 35%),radial-gradient(circle at 85% 15%,#5b962f 0%,rgba(91,150,47,0) 30%),linear-gradient(90deg,rgba(236,238,234,0),#e3e8dd)}
.hero-copy{position:absolute;left:80px;top:110px}
.hero-copy h1{font-size:44px;line-height:1.05;font-weight:900;color:var(--ink);letter-spacing:.5px}
.hero-copy p{font-family:"Roboto",sans-serif;font-size:19px;font-weight:500;color:#333;margin-top:14px;line-height:1.3;width:300px}
.hero-copy .btn{margin-top:38px}

/* community */
.community{position:absolute;top:520px;left:0;width:1200px;height:280px}
.community-img{left:132px;top:60px;width:268px;height:175px;background:linear-gradient(135deg,#c9a58a,#e5cdb6 50%,#b88c6e)}
.community-copy{position:absolute;left:448px;top:72px;width:620px}
.community-copy h2{font-size:18px;font-weight:700;color:var(--ink);letter-spacing:1px;display:flex;align-items:center;gap:10px}
.community-copy h2::after{content:"";width:30px;height:2px;background:var(--ink)}
.community-copy p{font-size:11px;margin-top:10px;line-height:1.6}
.community-copy .btn{margin-top:16px;padding:7px 14px;font-size:10px}

/* shop */
.shop{position:absolute;top:800px;left:0;width:1200px;height:510px;background:var(--soft)}
.shop .section-title{margin-top:52px}
.cards{position:absolute;top:104px;left:132px;display:flex;gap:24px}
.card{width:292px;height:314px;background:#fff;box-shadow:0 1px 4px rgba(0,0,0,.08);padding:16px}
.card .img{width:260px;height:220px}
.card .meta{display:flex;justify-content:space-between;align-items:flex-end;margin-top:16px}
.card h4{font-size:12px;font-weight:500;color:var(--ink)}
.card .price{font-size:12px;color:var(--ink);font-weight:700;font-family:"Roboto",sans-serif}
.card .btn{padding:6px 10px;font-size:9px;background:#eee;color:var(--ink)}
.img.tincture{background:linear-gradient(180deg,#f5f6fa,#d7dcef 40%,#4a5a9c 70%,#2c3670)}
.img.rollon{background:linear-gradient(180deg,#f7f7f7,#e5e5e5 25%,#1f1f25 40%,#2a2a33 85%,#f7f7f7)}
.img.lotion{background:linear-gradient(180deg,#f7f7f7,#ececec 20%,#1a1a1a 35%,#3d2a1a 70%,#f7f7f7)}
.view-all{position:absolute;top:462px;left:0;width:1200px;text-align:center}
.view-all .btn{background:#fff;color:var(--ink);border:1px solid var(--line);padding:6px 16px;font-size:10px}

/* benefits */
.benefits{position:absolute;top:1310px;left:0;width:1200px;height:450px}
.benefits-copy{position:absolute;left:132px;top:100px;width:420px}
.benefits-copy h2{font-size:21px;font-weight:900;color:var(--ink);line-height:1.25;letter-spacing:.5px}
.benefits-copy ul{list-style:none;margin-top:26px}
.benefits-copy li{display:flex;gap:12px;font-size:11px;line-height:1.55;margin-bottom:16px}
.benefits-copy li svg{flex:none;margin-top:2px}
.benefits-img{left:600px;top:20px;width:600px;height:400px;background:linear-gradient(120deg,#d7e2ec 0%,#c4d4e6 35%,#6f8fb8 60%,#dfe5ea 100%)}

/* knowledge */
.knowledge{position:absolute;top:1760px;left:0;width:1200px;height:460px;background:linear-gradient(180deg,#f6f6f6,#fafafa 60%,#f3f3f3)}
.knowledge .section-title{margin-top:24px}
.facts{position:absolute;top:66px;left:132px;display:flex;gap:24px}
.fact{width:292px}
.fact .img{width:292px;height:160px}
.fact h3{font-size:12px;font-weight:700;color:var(--ink);margin-top:22px}
.fact p{font-size:10.5px;margin-top:8px;line-height:1.55}
.img.leaf{background:linear-gradient(135deg,#1f5a2a,#4c9a3a 55%,#2e6d2e)}
.img.blocks{background:linear-gradient(135deg,#b33a2f,#c99a72 45%,#e4c8a4)}
.img.lab{background:linear-gradient(135deg,#2d4a67,#5f82a6 55%,#9cb8cf)}

/* notice */
.notice-wrap{position:absolute;top:2220px;left:0;width:1200px;height:120px;background:#fff}
.notice{position:absolute;left:140px;top:24px;width:920px;height:74px;border:1px solid var(--line);display:flex;align-items:center;padding:0 28px;gap:28px}
.notice .tag{background:var(--notice);color:#fff;font-family:"Roboto",sans-serif;font-weight:700;font-size:12px;padding:8px 22px;letter-spacing:.5px}
.notice p{font-size:10px;line-height:1.55;color:#666}

/* contact */
.contact{position:absolute;top:2340px;left:0;width:1200px;height:400px;background:#fff}
.form-panel{position:absolute;left:180px;top:20px;width:480px;height:340px;background:#fff;box-shadow:0 2px 10px rgba(0,0,0,.1);padding:26px 24px}
.form-panel h2{font-size:19px;font-weight:700;color:var(--ink)}
.fields{display:grid;grid-template-columns:1fr 1fr;gap:12px;margin-top:22px}
.field{height:30px;border:1px solid var(--line);font-size:10px;color:#aaa;padding:7px 10px;display:flex;justify-content:space-between;align-items:center}
.field.msg{grid-column:1 / 3;height:64px;align-items:flex-start}
.form-panel .btn{margin-top:20px;padding:8px 22px}
.map{left:680px;top:20px;width:340px;height:260px;background:linear-gradient(135deg,#e8eef0,#dfe7dc 40%,#e9e4d8 70%,#dbe4ee)}

/* footer */
.site-footer{position:absolute;top:2740px;left:0;width:1200px;height:212px;background:#f3f3f3;border-top:1px solid #e6e6e6}
.col{position:absolute;top:34px}
.col h4{font-size:13px;font-weight:700;color:var(--ink);margin-bottom:16px}
.col h4::after{content:"";display:block;width:24px;height:2px;background:var(--ink);margin-top:6px}
.col p,.col li{font-size:10px;line-height:1.6;color:#666}
.col ul{list-style:none}
.col li{margin-bottom:7px;display:flex;gap:8px;align-items:flex-start}
.socials{display:flex;gap:8px;margin-top:16px}
.socials span{width:18px;height:18px;border-radius:50%;background:#555}
.subscribe{width:200px;height:28px;border:1px solid var(--line);background:#fff;font-size:10px;color:#aaa;padding:6px 10px}
.copyright{position:absolute;top:2952px;left:0;width:1200px;height:44px;background:#e7e7e7;text-align:center;font-size:10px;color:#777;line-height:44px}
</style>
</head>
<body>

<header class="site-header">
  <div class="brand">QORTA LABS</div>
  <nav class="nav">
    <a class="active" href="#">Home</a>
    <a href="#">Community</a>
    <a href="#">Shop</a>
    <a href="#">Wholesale</a>
    <a href="#">Contact</a>
  </nav>
  <div class="login">
    <svg width="10" height="10" viewBox="0 0 10 10"><circle cx="5" cy="3" r="2.2" fill="#fff"/><path d="M1 10c0-2.5 1.8-4 4-4s4 1.5 4 4z" fill="#fff"/></svg>
    Log In
  </div>
  <div class="cart">
    <svg width="18" height="16" viewBox="0 0 18 16"><path d="M1 1h3l2 9h9l2-6H5" fill="none" stroke="#222" stroke-width="1.6"/><circle cx="7" cy="14" r="1.4" fill="#222"/><circle cx="14" cy="14" r="1.4" fill="#222"/></svg>
  </div>
</header>

<section class="hero">
  <div class="ph hero-art" role="img" aria-label="Hemp leaves beside amber CBD dropper bottles"></div>
  <div class="hero-copy">
    <h1>ROLLING ON<br>TO THE SCENE</h1>
    <p>We are proud to serve our community.</p>
    <a class="btn" href="#">Shop Now</a>
  </div>
</section>

<section class="community">
  <div class="ph community-img" role="img" aria-label="Hands joined together in a circle"></div>
  <div class="community-copy">
    <h2>COMMUNITY</h2>
    <p>Our goal when creating this company was to help people be able to live a better life. That goal has been our focus from day one and it shapes every product we make. We believe plant wellness should be honest, tested and easy to reach for anyone who needs it, so we keep asking "how can we help?"</p>
    <p>We want to help those who are building something, whether it is a career, a family or a healthier way of life. We are here to provide the products you trust, and if there is something we can do to help you with your community, let us know.</p>
    <a class="btn" href="#">Read More</a>
  </div>
</section>

<section class="shop">
  <h2 class="section-title">SHOP</h2>
  <div class="cards">
    <div class="card">
      <div class="img tincture" role="img" aria-label="Rows of blue CBD tincture bottles"></div>
      <div class="meta"><div><h4>Tincture</h4><div class="price">$49.00</div></div><a class="btn" href="#">SHOP NOW</a></div>
    </div>
    <div class="card">
      <div class="img rollon" role="img" aria-label="Black CBD roll-on applicator"></div>
      <div class="meta"><div><h4>Roll-On Ointment</h4><div class="price">$34.00</div></div><a class="btn" href="#">SHOP NOW</a></div>
    </div>
    <div class="card">
      <div class="img lotion" role="img" aria-label="Dark CBD lotion bottle"></div>
      <div class="meta"><div><h4>Lotion</h4><div class="price">$29.00</div></div><a class="btn" href="#">SHOP NOW</a></div>
    </div>
  </div>
  <div class="view-all"><a class="btn" href="#">View All &nbsp;→</a></div>
</section>

<section class="benefits">
  <div class="benefits-copy">
    <h2>DISCOVER THE BENEFITS OF<br>QORTA LABS CBD</h2>
    <ul>
      <li><svg width="12" height="12" viewBox="0 0 12 12"><circle cx="6" cy="6" r="6" fill="#222"/><path d="M3.3 6.2l1.8 1.8 3.6-3.8" fill="none" stroke="#fff" stroke-width="1.4"/></svg>All of our products are tested to ensure the finest quality CBD available.</li>
      <li><svg width="12" height="12" viewBox="0 0 12 12"><circle cx="6" cy="6" r="6" fill="#222"/><path d="M3.3 6.2l1.8 1.8 3.6-3.8" fill="none" stroke="#fff" stroke-width="1.4"/></svg>Choose from a wide variety of products and flavors including concentrates, edibles, tinctures, vape pens, body creams, salves and more.</li>
      <li><svg width="12" height="12" viewBox="0 0 12 12"><circle cx="6" cy="6" r="6" fill="#222"/><path d="M3.3 6.2l1.8 1.8 3.6-3.8" fill="none" stroke="#fff" stroke-width="1.4"/></svg>We use CO2 extraction and a chemical-free extraction process that is environmentally friendly and safe for all of our hemp CBD oil.</li>
    </ul>
  </div>
  <div class="ph benefits-img" role="img" aria-label="Lab technician in gloves handling a dropper and sample vials"></div>
</section>

<section class="knowledge">
  <h2 class="section-title">KNOWLEDGE IS POWER</h2>
  <div class="facts">
    <div class="fact">
      <div class="img leaf" role="img" aria-label="Green hemp leaf close up"></div>
      <h3>WHAT IS CBD?</h3>
      <p>Cannabidiol, also known as CBD, is a plant compound found in hemp. Unlike THC it does not cause intoxication and is widely used in oils, creams and edibles for everyday wellness.</p>
    </div>
    <div class="fact">
      <div class="img blocks" role="img" aria-label="Wooden letter blocks on a table"></div>
      <h3>IS IT LEGAL?</h3>
      <p>Because all of our CBD products are derived from agricultural hemp with less than 0.3% THC, they are legal to buy and use across all fifty states in the United States.</p>
    </div>
    <div class="fact">
      <div class="img lab" role="img" aria-label="Scientist examining a sample in a lab"></div>
      <h3>IS IT SAFE?</h3>
      <p>CBD has a remarkable safety profile and Qorta Labs goes further to ensure high quality, testing each batch in our own lab so you always know what is in the bottle.</p>
    </div>
  </div>
</section>

<section class="notice-wrap">
  <div class="notice">
    <span class="tag">NOTICE</span>
    <p>The statements regarding these products have not been evaluated by the Food and Drug Administration. These products are not intended to diagnose, treat, cure or prevent any disease. Results from products may vary.</p>
  </div>
</section>

<section class="contact">
  <div class="form-panel">
    <h2>Let's Get Started</h2>
    <div class="fields">
      <div class="field">Name</div>
      <div class="field">Email</div>
      <div class="field">Phone</div>
      <div class="field">Subject Type <span>▾</span></div>
      <div class="field msg">Message</div>
    </div>
    <a class="btn" href="#">Submit</a>
  </div>
  <div class="ph map" role="img" aria-label="Street map showing the Qorta Labs location"></div>
</section>

<footer class="site-footer">
  <div class="col" style="left:132px;width:200px">
    <div class="brand" style="font-size:17px;margin-bottom:10px">QORTA LABS</div>
    <p>Lab-grown care for everyday people, made in small batches.</p>
    <div class="socials"><span></span><span></span><span></span><span></span></div>
  </div>
  <div class="col" style="left:368px;width:180px">
    <h4>Quick Link</h4>
    <ul><li>About Us</li><li>Customer Satisfaction</li><li>Shipping &amp; Return Policy</li><li>Privacy Policy</li><li>Terms of Service</li></ul>
  </div>
  <div class="col" style="left:580px;width:210px">
    <h4>Connect Info</h4>
    <ul>
      <li><svg width="10" height="12" viewBox="0 0 10 12"><path d="M5 0a4 4 0 014 4c0 3-4 8-4 8S1 7 1 4a4 4 0 014-4z" fill="#555"/><circle cx="5" cy="4" r="1.4" fill="#f3f3f3"/></svg>214 Larkfield Road, Suite 9,<br>Denver, CO 80204</li>
      <li><svg width="10" height="10" viewBox="0 0 10 10"><path d="M2 0l2 2.5-1 1.2a6 6 0 003.3 3.3l1.2-1L10 8l-1.5 2C4 10 0 6 0 1.5z" fill="#555"/></svg>(303) 555-0148</li>
      <li><svg width="11" height="9" viewBox="0 0 11 9"><rect x=".5" y=".5" width="10" height="8" fill="none" stroke="#555"/><path d="M.5.5l5 4 5-4" fill="none" stroke="#555"/></svg>hello@qortalabs-example.com</li>
    </ul>
  </div>
  <div class="col" style="left:820px;width:220px">
    <h4>Subscribe Now</h4>
    <div class="subscribe">Email Address</div>
    <a class="btn" href="#" style="margin-top:10px;padding:7px 16px">Subscribe</a>
  </div>
</footer>
<div class="copyright">Copyright © 2021 Qorta Labs. All Rights Reserved</div>

</body>
</html>
```